Fabric Softener

We need fabric softener. Bottle picture attached for reference. Color of bottle can be proposed as well. Normally bottle is pink and blue color

Logo is also attached that shall be used.
Updates

Need extra days to review

Low designer entries

Target Market(s)

Niche

Font styles to use
Sans Serif

Requirements
Must have
• Fabric, Brightness, Nature
Nice to have
• Good colors
Should not have
• Adults

```html
<!DOCTYPE html>
<html lang="en">
<head>
<meta charset="utf-8">
<title>Lumena Premium Fabric Softener</title>
<link rel="stylesheet" href="https://fonts.googleapis.com/css2?family=Baloo+2:wght@600;800&family=Open+Sans:wght@700&display=swap">
<style>
  :root {
    --bottle-purple: #6f5aa9;
    --bottle-light: #8b78bd;
    --bottle-dark: #574690;
    --cap-white: #f4f4f4;
    --cap-shade: #dcdcdc;
    --title-purple: #6a2a93;
    --title-fill-top: #ffffff;
    --title-fill-bottom: #c9b3e0;
    --sky-top: #7fb0e6;
    --sky-deep: #3c66b1;
    --grass: #9fb13a;
    --ink: #1b1b2a;
    --white: #ffffff;
  }
  html, body {
    margin: 0;
    padding: 0;
    overflow: hidden;
    background: var(--white);
  }
  .canvas {
    position: relative;
    width: 734px;
    height: 1200px;
    overflow: hidden;
    background: var(--white);
  }
  .bottle {
    position: absolute;
    inset: 0;
  }
  .brand-name {
    font-family: "Baloo 2", sans-serif;
    font-weight: 800;
    font-size: 60px;
    fill: var(--white);
  }
  .title {
    font-family: "Baloo 2", sans-serif;
    font-weight: 800;
    paint-order: stroke fill;
    stroke: var(--title-purple);
    stroke-linejoin: round;
  }
  .title-premium { font-size: 56px; stroke-width: 9px; }
  .title-fabric { font-size: 128px; stroke-width: 14px; letter-spacing: -2px; }
  .title-softener { font-size: 120px; stroke-width: 14px; letter-spacing: -3px; }
  .benefits {
    font-family: "Baloo 2", sans-serif;
    font-weight: 800;
    font-size: 21px;
    fill: var(--ink);
    paint-order: stroke fill;
    stroke: var(--white);
    stroke-width: 3px;
  }
  .volume {
    font-family: "Open Sans", sans-serif;
    font-weight: 700;
    font-size: 19px;
    fill: var(--ink);
  }
</style>
</head>
<body>
<main class="canvas">
  <svg class="bottle" viewBox="0 0 734 1200" width="734" height="1200" xmlns="http://www.w3.org/2000/svg">
    <defs>
      <linearGradient id="bodyShade" x1="0" y1="0" x2="1" y2="0">
        <stop offset="0" stop-color="var(--bottle-dark)"/>
        <stop offset="0.15" stop-color="var(--bottle-purple)"/>
        <stop offset="0.55" stop-color="var(--bottle-light)"/>
        <stop offset="0.85" stop-color="var(--bottle-purple)"/>
        <stop offset="1" stop-color="var(--bottle-dark)"/>
      </linearGradient>
      <linearGradient id="capShade" x1="0" y1="0" x2="1" y2="0">
        <stop offset="0" stop-color="var(--cap-shade)"/>
        <stop offset="0.5" stop-color="var(--cap-white)"/>
        <stop offset="1" stop-color="var(--cap-shade)"/>
      </linearGradient>
      <linearGradient id="scene" x1="0" y1="0" x2="0.7" y2="1">
        <stop offset="0" stop-color="var(--sky-top)"/>
        <stop offset="0.5" stop-color="var(--sky-deep)"/>
        <stop offset="0.8" stop-color="#8fb5d8"/>
        <stop offset="1" stop-color="var(--grass)"/>
      </linearGradient>
      <linearGradient id="titleFill" x1="0" y1="0" x2="0" y2="1">
        <stop offset="0.4" stop-color="var(--title-fill-top)"/>
        <stop offset="1" stop-color="var(--title-fill-bottom)"/>
      </linearGradient>
    </defs>

    <rect class="cap" x="257" y="46" width="182" height="165" rx="14" fill="url(#capShade)"/>
    <rect class="cap-collar" x="225" y="195" width="246" height="60" rx="10" fill="url(#capShade)"/>

    <path class="bottle-body" fill="url(#bodyShade)"
      d="M228 250 C225 330 140 400 100 520 C70 610 70 700 72 800
         L72 1120 C72 1168 100 1184 150 1184 L590 1184
         C640 1184 675 1168 676 1120 L676 760
         C676 620 650 500 600 420 C540 330 470 310 468 250 Z"/>

    <ellipse class="handle-hole" cx="258" cy="534" rx="38" ry="108" transform="rotate(24 258 534)" fill="var(--white)"/>

    <text class="brand-name" x="472" y="626" text-anchor="middle">Lumena</text>

    <path class="label-scene" role="img" aria-label="Photo of a stack of white towels under a sunny blue sky above green grass"
      fill="url(#scene)"
      d="M80 800 C80 780 95 772 115 772 L300 772 C360 772 380 700 460 690
         L600 688 C622 688 634 700 634 722 L634 1118 C634 1138 622 1146 600 1146
         L110 1146 C90 1146 80 1136 80 1118 Z"/>

    <text class="title title-premium" x="424" y="795" text-anchor="middle" fill="url(#titleFill)">Premium</text>
    <text class="title title-fabric" x="376" y="900" text-anchor="middle" fill="url(#titleFill)">Fabric</text>
    <text class="title title-softener" x="372" y="1043" text-anchor="middle" fill="url(#titleFill)">Softener</text>

    <g class="benefits" transform="rotate(-5 445 1110)">
      <text x="345" y="1088">Reduces Static Cling</text>
      <text x="345" y="1113">Softens &amp; Freshens</text>
      <text x="345" y="1138">Helps Repel Pet Hair</text>
    </g>

    <text class="volume" x="194" y="1110">50 FL OZ</text>
  </svg>
</main>
</body>
</html>
```